Flyer-Design für Heizungsbau
Zielgruppe
Wir sind ein junges, kompetentes und zertifiziertes Fachbetrieb und bieten Beratung, Fachplanung und fachmännische Installation von Wärmepumpen, Klimaanlagen und Lüftungsanlagen. Unsere Zielgruppe sind Eigentümer von Bestandsgebäuden oder Neubauten (hauptsächlich Privatkunden in mittlerem oder höherem Alter), welche eine Heizungssanierung für Heizkostenreduzierung oder neue Heizinstallation (Wärmepumpen), und/oder mehr Komfort bzw. Luftqualität in ihren Zuhause wünschen (Klima und Lüftung).
Aufgabenstellung
Schwerpunkte: 1. Ersparnis an Heizkosten, 2. Wohlgefühl und 3. Klimaschutz

```html
<!DOCTYPE html>
<html lang="de">
<head>
<meta charset="utf-8">
<title>Luftwerk – Flyer Vorder- und Rückseite</title>
<link rel="stylesheet" href="https://fonts.googleapis.com/css2?family=Nunito+Sans:wght@400;600;700&family=Roboto+Condensed:wght@300;400;700&display=swap">
<style>
  :root {
    --navy: #16387a;
    --sky: #3f9ad8;
    --sky-light: #62b0e6;
    --band: #5aa8df;
    --band-deep: #3d8fcf;
    --circle: #3e95d6;
    --icon: #1b4c9c;
    --ink: #1f2f55;
    --paper: #ffffff;
    --stage: #e6e8eb;
  }
  * { box-sizing: border-box; margin: 0; padding: 0; }
  html, body { width: 1200px; height: 2350px; overflow: hidden; }
  body { background: var(--stage); position: relative; font-family: "Nunito Sans", sans-serif; }

  .page { position: absolute; left: 310px; width: 580px; height: 1155px; background: var(--paper); overflow: hidden; box-shadow: 0 2px 8px rgba(0,0,0,.12); }
  .page--front { top: 13px; }
  .page--back { top: 1182px; }

  /* front */
  .headline { position: absolute; left: 28px; top: 16px; font-size: 72px; line-height: 70px; font-weight: 600; color: var(--sky); letter-spacing: -0.5px; }
  .headline .strong { color: var(--navy); }
  .photo { position: absolute; }
  .photo--couple { left: 0; top: 170px; width: 580px; height: 378px; background: linear-gradient(135deg, #d9d4cc 0%, #b9b1a6 45%, #8a7f76 100%); }
  .cta { position: absolute; left: 0; width: 100%; text-align: center; font-family: "Roboto Condensed", sans-serif; font-weight: 700; color: var(--navy); }
  .cta--front { top: 560px; font-size: 21px; }
  .phone-big { position: absolute; top: 594px; left: 0; width: 100%; display: flex; justify-content: center; align-items: center; gap: 12px; color: var(--sky); font-family: "Roboto Condensed", sans-serif; font-weight: 700; font-size: 40px; letter-spacing: 1px; }
  .ico-box { width: 30px; height: 30px; border-radius: 5px; background: var(--sky); display: flex; align-items: center; justify-content: center; }
  .blue-field { position: absolute; left: 0; top: 643px; width: 580px; height: 387px; background: radial-gradient(ellipse at 50% 40%, #8cc8ef 0%, var(--band) 55%, var(--band-deep) 100%); }
  .bubble { position: absolute; border-radius: 50%; background: var(--circle); color: #fff; display: flex; align-items: center; justify-content: center; text-align: center; font-weight: 400; line-height: 1.05; box-shadow: 0 0 24px rgba(255,255,255,.45); }
  .bubble--klimaschutz { left: 6px; top: 6px; width: 120px; height: 120px; font-size: 28px; }
  .bubble--ersparnis { left: 75px; top: 200px; width: 160px; height: 160px; font-size: 30px; }
  .bubble--wohlgefuehl { left: 352px; top: 204px; width: 145px; height: 145px; font-size: 32px; }
  .intro { position: absolute; left: 160px; top: 26px; width: 400px; font-family: "Roboto Condensed", sans-serif; font-size: 15px; line-height: 21px; color: #fff; }
  .intro b { color: var(--navy); font-weight: 700; }
  .footer { position: absolute; left: 0; width: 100%; height: 125px; }
  .page--front .footer { top: 1030px; }
  .page--back .footer { top: 1030px; }
  .tagline { position: absolute; left: 30px; top: 36px; font-size: 17px; line-height: 21px; color: var(--sky); }
  .tagline .lead { color: var(--navy); font-weight: 600; }
  .brand { position: absolute; display: flex; align-items: center; gap: 14px; color: var(--sky); font-weight: 600; }
  .brand-dot { border-radius: 50%; background: var(--icon); }
  .page--front .brand { right: 28px; top: 30px; font-size: 46px; }
  .page--front .brand-dot { width: 52px; height: 52px; }
  .page--back .brand { right: 34px; top: 34px; font-size: 30px; }
  .page--back .brand-dot { width: 38px; height: 38px; }

  /* back */
  .photo--installer { left: 0; top: 0; width: 288px; height: 268px; background: linear-gradient(160deg, #2d6fa6 0%, #a98d56 55%, #5d4a32 100%); }
  .photo--units { left: 288px; top: 0; width: 292px; height: 268px; background: linear-gradient(160deg, #9a9c9e 0%, #6f7173 60%, #4d4f51 100%); }
  .bubble--kuehlen { left: 388px; top: 218px; width: 140px; height: 140px; font-size: 28px; }
  .promise { position: absolute; left: 38px; top: 318px; width: 500px; }
  .promise h2 { font-size: 25px; font-weight: 600; color: var(--ink); margin-bottom: 8px; }
  .promise-item { margin-bottom: 9px; }
  .promise-item h3 { font-size: 20px; font-weight: 400; color: var(--sky); line-height: 26px; }
  .promise-item p { font-family: "Roboto Condensed", sans-serif; font-size: 15px; color: var(--ink); line-height: 18px; }
  .service-band { position: absolute; left: 0; top: 595px; width: 580px; height: 292px; background: radial-gradient(ellipse at 50% 35%, #8cc8ef 0%, var(--band) 55%, var(--band-deep) 100%); border-bottom: 5px solid #2a5a95; }
  .service { position: absolute; top: 24px; width: 170px; }
  .service:nth-child(1) { left: 38px; }
  .service:nth-child(2) { left: 226px; }
  .service:nth-child(3) { left: 414px; width: 150px; }
  .service-icon { width: 76px; height: 76px; border-radius: 50%; background: var(--icon); display: flex; align-items: center; justify-content: center; margin-bottom: 14px; box-shadow: 0 0 16px rgba(255,255,255,.5); }
  .service h3 { font-size: 27px; font-weight: 400; color: var(--navy); line-height: 32px; }
  .service p { font-family: "Roboto Condensed", sans-serif; font-size: 15px; line-height: 20px; color: #fff; margin-top: 4px; }
  .cta--back { top: 940px; font-size: 20px; }
  .contact-row { position: absolute; top: 982px; left: 0; width: 100%; display: flex; justify-content: center; gap: 34px; font-family: "Roboto Condensed", sans-serif; font-weight: 700; font-size: 21px; color: var(--navy); }
  .contact { display: flex; align-items: center; gap: 8px; }
  .contact .ico-box { width: 28px; height: 28px; }
</style>
</head>
<body>

<section class="page page--front">
  <h1 class="headline"><span class="strong">Ihr Klima</span> ist<br>unser Auftrag!</h1>
  <div class="photo photo--couple" role="img" aria-label="Foto: Mann trägt ein Klimagerät ins Wohnzimmer, Frau auf dem Sofa jubelt"></div>
  <p class="cta cta--front">Vereinbaren Sie einen unverbindlichen Beratungstermin</p>
  <div class="phone-big">
    <span class="ico-box"><svg width="18" height="18" viewBox="0 0 24 24"><path fill="#fff" d="M6.6 10.8a15.1 15.1 0 0 0 6.6 6.6l2.2-2.2c.3-.3.7-.4 1-.2 1.1.4 2.3.6 3.6.6.6 0 1 .4 1 1V20c0 .6-.4 1-1 1A17 17 0 0 1 3 4c0-.6.4-1 1-1h3.5c.6 0 1 .4 1 1 0 1.3.2 2.5.6 3.6.1.3 0 .7-.2 1z"/></svg></span>
    <span>06172/4958302</span>
  </div>
  <div class="blue-field">
    <div class="bubble bubble--klimaschutz">Klima-<br>schutz</div>
    <p class="intro">Luftwerk GmbH ist Ihr zuverlässiger Partner im Bereich <b>Klima-, Kälte- und Lüftungstechnik</b>. Als <b>zertifiziertes Fachunternehmen</b> bieten wir Ihnen schlüsselfertige Kälte-, Klima- und Lüftungsanlagen von marktführenden Herstellern. Von Installations- und Instandhaltungsleistungen bis zu Hygieneinspektionen nach <b>VDI 6022</b> steht unser zertifiziertes Fachpersonal Ihnen gerne zur Seite.</p>
    <div class="bubble bubble--ersparnis">Ersparnis<br>an Heiz-<br>kosten</div>
    <div class="bubble bubble--wohlgefuehl">Wohl-<br>gefühl</div>
  </div>
  <footer class="footer">
    <p class="tagline"><span class="lead">Ihr Fachbetrieb für</span><br>Klimaanlagen und<br>Installation</p>
    <div class="brand"><span class="brand-dot"></span><span>Luftwerk</span></div>
  </footer>
</section>

<section class="page page--back">
  <div class="photo photo--installer" role="img" aria-label="Foto: Monteurin hält ein Klimagerät"></div>
  <div class="photo photo--units" role="img" aria-label="Foto: Innen- und Außeneinheit einer Wärmepumpe"></div>
  <div class="bubble bubble--kuehlen">Kühlen<br>&amp; Heizen</div>
  <div class="promise">
    <h2>Unser Versprechen:</h2>
    <div class="promise-item"><h3>Schnelle Installation</h3><p>Garantierte Installation innerhalb von wenigen Wochen</p></div>
    <div class="promise-item"><h3>Festpreis</h3><p>Alle unsere Angebote zum Festpreis keine Änderung durch mehr Aufwand</p></div>
    <div class="promise-item"><h3>Faire Preise</h3><p>Von fairen Preisen überzeugt, bieten wir ein faires Preis-/Leistungsverhältnis an</p></div>
    <div class="promise-item"><h3>Höchste Qualität</h3><p>Wir führen jede Arbeit mit höchster Sorgfalt und Qualität durch</p></div>
  </div>
  <div class="service-band">
    <div class="service">
      <div class="service-icon"><svg width="40" height="40" viewBox="0 0 24 24"><path fill="#fff" d="M21.7 6.3a6 6 0 0 1-7.9 7.3L6 21.4a2 2 0 0 1-2.8-2.8L11 10.8a6 6 0 0 1 7.3-7.9l-3.6 3.6.7 2.9 2.9.7z"/></svg></div>
      <h3>Installation</h3>
      <p>Wir installieren Ihre Klimaanlage fachmännisch und mit höchster Präzision</p>
    </div>
    <div class="service">
      <div class="service-icon"><svg width="38" height="38" viewBox="0 0 24 24"><path fill="#fff" d="M2 3h3.2l.8 3H22l-2.4 8H7.6l.5 2H19v2H6.6L3.8 5H2z"/><circle cx="9" cy="20.5" r="1.6" fill="#fff"/><circle cx="17" cy="20.5" r="1.6" fill="#fff"/></svg></div>
      <h3>Verkauf</h3>
      <p>Bei uns erhalten Sie Ihr Klimagerät zu einem günstigen Preis. Wir verkaufen nur hochwertige Anlagen</p>
    </div>
    <div class="service">
      <div class="service-icon"><svg width="40" height="40" viewBox="0 0 24 24"><path fill="#fff" d="M21.7 6.3a6 6 0 0 1-7.9 7.3L6 21.4a2 2 0 0 1-2.8-2.8L11 10.8a6 6 0 0 1 7.3-7.9l-3.6 3.6.7 2.9 2.9.7z"/></svg></div>
      <h3>Wartung</h3>
      <p>Die notwendigen Wartungen an Ihrer Klimaanlage führen wir professionell durch</p>
    </div>
  </div>
  <p class="cta cta--back">Vereinbaren Sie einen unverbindlichen Beratungstermin:</p>
  <div class="contact-row">
    <span class="contact"><span class="ico-box"><svg width="16" height="16" viewBox="0 0 24 24"><path fill="#fff" d="M6.6 10.8a15.1 15.1 0 0 0 6.6 6.6l2.2-2.2c.3-.3.7-.4 1-.2 1.1.4 2.3.6 3.6.6.6 0 1 .4 1 1V20c0 .6-.4 1-1 1A17 17 0 0 1 3 4c0-.6.4-1 1-1h3.5c.6 0 1 .4 1 1 0 1.3.2 2.5.6 3.6.1.3 0 .7-.2 1z"/></svg></span>06172/4958302</span>
    <span class="contact"><span class="ico-box"><svg width="18" height="18" viewBox="0 0 24 24"><rect x="3" y="6" width="18" height="12" rx="1" fill="none" stroke="#fff" stroke-width="2"/><path d="M3 7l9 6 9-6" fill="none" stroke="#fff" stroke-width="2"/></svg></span>info@luftwerk-klima.de</span>
  </div>
  <footer class="footer">
    <p class="tagline"><span class="lead">Ihr Fachbetrieb für</span><br>Klimaanlagen und<br>Installation</p>
    <div class="brand"><span class="brand-dot"></span><span>Luftwerk</span></div>
  </footer>
</section>

</body>
</html>
```